Re designing of website of VELTARO Pens, an International stationary brand

We would like to re design our existing website veltaropens.com. We are leading manufacturers and exporters of stationary products. Our existence is global -selling and marketing in all 5 continents.

We are a 35year old group with focus on high quality, innovative designs and state of art manufacturing setup.

Client satisfaction by committed service and trust are the roots of our organisation.

We would like to see a website which focuses on our brand Veltaro and must have an international appeal. Our target buyers would be Agents, distributors and wholesalers in various countries. Content would be similar to our existing website but designing and outlook needs to be totally different.

For the outlook we do like the following websites from our industry which can be used to draw inspiration.
1. www.quillbrookstationery.example
2. www.marovipen.example
3. www.tulsbergpen.example

The homepage need not be focused on the product but must emphasis on the branding of Veltaro, our existence of 35years along with international presence and quality standards maintained by our organisation.
Updates

Reason: Would like to see some more concepts and designs as per artwork attached.

Target Market(s)

Wholesalers, Agents and Distributors in all countries around the world. Target market is global

Number of Pages Required

1 page

Font styles to use
Sans Serif

Requirements
Must have
• Focus on Branding, High Quality Standards, Customer Loyalty
Nice to have
• Like the outlook of the websites
• www.tulsbergpen.example
• www.quillbrookstationery.example
• www.marovipen.example
Should not have
• Don't like the outlook of our present website www.veltaropens.com
• It doesn't justify our brand or our product

```html
<!DOCTYPE html>
<html lang="en">
<head>
<meta charset="utf-8">
<title>Veltaro Pens – World Class Writing Instruments</title>
<link rel="stylesheet" href="https://fonts.googleapis.com/css2?family=Source+Sans+3:wght@200;300;400;600;700&family=Open+Sans:wght@400;600;700&family=Oswald:wght@300;400&family=Raleway:wght@500;600&display=swap">
<style>
:root{
  --red:#dd0a0c;
  --red-band:#e11b22;
  --ink:#333;
  --muted:#555;
  --light:#999;
  --hero-bg:#f0efec;
  --page:#f4f4f4;
  --gold:#e2a72a;
  --gold-dark:#c98c12;
  --white:#fff;
  --black:#0b0b0b;
  --line:#e4e4e4;
}
*{box-sizing:border-box;margin:0;padding:0}
html,body{width:787px;height:1200px;overflow:hidden}
body{background:var(--white);font-family:"Open Sans",Arial,sans-serif;color:var(--ink);position:relative}
.abs{position:absolute}

/* header */
.site-header{position:absolute;left:0;top:0;width:787px;height:67px;background:var(--red)}
.brand{position:absolute;left:57px;top:14px;display:flex;align-items:center;gap:8px}
.brand-mark{width:36px;height:36px;background:var(--white)}
.brand-name{font-family:"Source Sans 3",sans-serif;font-weight:700;font-size:31px;color:var(--white);letter-spacing:.5px;line-height:1}
.main-nav a{position:absolute;top:29px;font-family:"Open Sans",sans-serif;font-weight:600;font-size:9.4px;color:var(--white);text-decoration:none;letter-spacing:.2px;white-space:nowrap}
.main-nav a.active{font-weight:700}
.main-nav a.active::after{content:"";position:absolute;left:0;right:0;top:35px;height:2px;background:var(--white)}
.caret{display:inline-block;border:3px solid transparent;border-top-color:var(--white);border-bottom:0;margin-left:2px;vertical-align:2px}
.lang{position:absolute;left:664px;top:26px;width:66px;height:20px;background:#c30a0c;color:var(--white);font-weight:700;font-size:9px;display:flex;align-items:center;justify-content:center;gap:4px}

/* hero */
.hero{position:absolute;left:0;top:67px;width:787px;height:327px;background:radial-gradient(ellipse at 40% 45%,#f8f7f5 0%,var(--hero-bg) 60%,#e6e4e0 100%);overflow:hidden}
.hero-orbit{position:absolute;left:0;top:0}
.hero-kicker{position:absolute;left:56px;top:52px;font-family:"Source Sans 3",sans-serif;font-weight:400;font-size:23px;color:#222;letter-spacing:1px}
.hero-title{position:absolute;left:54px;top:70px;font-family:"Source Sans 3",sans-serif;font-weight:400;font-size:55px;color:var(--red);letter-spacing:1px;line-height:1}
.hero-sub{position:absolute;right:384px;top:113px;font-family:"Source Sans 3",sans-serif;font-weight:200;font-size:39px;color:var(--red);letter-spacing:1.5px;line-height:1}
.hero-copy{position:absolute;left:57px;top:162px;font-size:10.8px;line-height:14.5px;color:#222;letter-spacing:.6px}
.hero-copy strong{font-weight:700}
.btn-outline{position:absolute;left:57px;top:222px;width:135px;height:28px;border:1.5px solid var(--red);color:var(--red);font-weight:700;font-size:8.6px;display:flex;align-items:center;padding-left:15px;letter-spacing:.2px}
.btn-outline svg{position:absolute;right:10px;top:9px}
.hero-dots{position:absolute;left:57px;top:282px;display:flex;gap:6px}
.hero-dots span{width:9px;height:9px;border:1px solid #777;border-radius:50%}
.hero-dots span.on{border-color:var(--red);border-width:1.5px}
.hero-arrow{position:absolute;top:166px}
.hero-product{position:absolute;left:500px;top:15px;width:230px;height:300px;background:linear-gradient(90deg,#d9359c 0%,#ef7b1c 25%,#2c4fd0 50%,#d6242a 72%,#4b4b4b 95%);opacity:.85;border-radius:4px}

/* welcome + events */
.intro{position:absolute;left:0;top:394px;width:787px;height:266px;background:var(--white)}
.section-title{font-family:"Source Sans 3",sans-serif;font-weight:400;font-size:21px;color:#333;letter-spacing:.5px;line-height:1}
.section-title em{font-style:normal;color:var(--red)}
.welcome-title{position:absolute;left:57px;top:44px}
.welcome-text{position:absolute;left:57px;top:78px;width:345px;font-size:8.6px;line-height:14.6px;color:#444}
.welcome-text p+p{margin-top:5px}
.divider{position:absolute;left:420px;top:45px;width:1px;height:170px;background:var(--line)}
.events-title{position:absolute;left:439px;top:44px}
.round-btn{position:absolute;top:41px;width:20px;height:20px;border:1px solid #ddd;border-radius:50%}
.round-btn svg{position:absolute;left:6px;top:5px}
.sort-options{position:absolute;right:57px;top:69px;font-size:7px;font-style:italic;color:#666;letter-spacing:.2px}
.month{position:absolute;left:441px;top:78px;font-family:"Oswald",sans-serif;font-weight:400;font-size:16px;color:#bbb}
.sort-row{position:absolute;right:57px;top:82px;display:flex;align-items:center;gap:5px;font-size:6.4px;color:#666}
.sort-row .lbl{color:#bbb}
.sort-row .chip{background:#bbb;color:var(--white);padding:1px 3px;font-style:italic;font-weight:700}
.sort-row .sep{width:1px;height:10px;background:#ccc;margin:0 2px}
.event-list{position:absolute;left:439px;top:103px;width:291px;height:93px;border:1px solid #e6e6e6;background:#fafafa}
.event{position:absolute;left:0;width:290px;height:46px;border-left:3px solid var(--gold)}
.event+.event{border-left-color:var(--red);border-top:1px solid #e6e6e6}
.event-date{position:absolute;left:9px;top:7px;font-family:"Oswald",sans-serif;color:#aaa;line-height:1}
.event-date .dow{font-size:5px;display:block}
.event-date .day{font-size:20px}
.event-date .mon{font-size:6px;display:block}
.event-date .range{position:absolute;left:24px;top:8px;font-size:8px;white-space:nowrap}
.event-name{position:absolute;left:52px;top:8px;font-family:"Oswald",sans-serif;font-weight:400;font-size:12px;color:#555}
.event-meta{position:absolute;left:52px;top:24px;font-size:6.5px;color:#999;line-height:9px;width:170px}
.event-meta i{font-size:5.4px}
.event-meta b{color:#666;font-weight:600}

/* exporting countries */
.countries{position:absolute;left:0;top:660px;width:787px;height:197px;background:var(--red-band);overflow:hidden;color:var(--white)}
.countries-map{position:absolute;inset:0;background:radial-gradient(ellipse at 40% 55%,rgba(150,0,0,.35) 0%,rgba(150,0,0,.12) 45%,rgba(0,0,0,0) 75%)}
.countries-title{position:absolute;left:0;width:787px;top:33px;text-align:center;font-family:"Source Sans 3",sans-serif;font-weight:300;font-size:21px;letter-spacing:1px}
.countries-rule{position:absolute;left:57px;top:64px;width:673px;height:1px;background:rgba(255,255,255,.45)}
.cloud{position:absolute;left:57px;top:72px;width:673px;font-family:"Open Sans",sans-serif;font-weight:600;text-transform:uppercase}
.cloud-row{display:flex;justify-content:center;align-items:baseline;gap:13px;height:17px;white-space:nowrap}
.cloud-row span{font-size:7.6px}
.cloud-row span.lg{font-size:12.5px}

/* features */
.features{position:absolute;left:0;top:857px;width:787px;height:276px;background:var(--page)}
.card{position:absolute;top:30px;width:167px;height:213px;background:var(--white);text-align:center}
.card.highlight{box-shadow:0 12px 14px -8px rgba(0,0,0,.35)}
.card-title{position:absolute;left:0;right:0;top:12px;font-family:"Raleway",sans-serif;font-weight:500;font-size:11.6px;line-height:14px;color:#222;letter-spacing:.2px}
.card.highlight .card-title{color:var(--gold)}
.seal{position:absolute;left:42px;top:45px;width:83px;height:83px;border-radius:50%;background:radial-gradient(circle at 40% 35%,#fbe08a 0%,var(--gold) 55%,var(--gold-dark) 100%)}
.card-text{position:absolute;left:12px;right:12px;top:138px;font-size:8.6px;line-height:15px;color:#333}
.plus{position:absolute;left:76px;top:188px;width:15px;height:15px;background:var(--gold);color:var(--white);font-weight:700;font-size:13px;line-height:15px}

/* footer */
.site-footer{position:absolute;left:0;top:1133px;width:787px;height:67px;background:var(--black);color:var(--white)}
.footer-brand{position:absolute;left:57px;top:21px;display:flex;align-items:center;gap:6px}
.footer-brand .brand-mark{width:24px;height:24px}
.footer-brand .brand-name{font-size:20px}
.copyright{position:absolute;left:178px;top:29px;font-size:8px;letter-spacing:.2px}
.social{position:absolute;left:626px;top:24px;display:flex;gap:5px}
.social span{width:17px;height:17px;border-radius:50%;background:#4a4a4a}
</style>
</head>
<body>

<header class="site-header">
  <div class="brand"><span class="brand-mark"></span><span class="brand-name">VELTARO</span></div>
  <nav class="main-nav">
    <a class="active" style="left:292px">HOME</a>
    <a style="left:340px">ABOUT US</a>
    <a style="left:403px">PRODUCTS<span class="caret"></span></a>
    <a style="left:467px">CAREERS</a>
    <a style="left:525px">ENQUIRY FORM</a>
    <a style="left:607px">CONTACT</a>
  </nav>
  <div class="lang">ENGLISH <span class="caret"></span></div>
</header>

<section class="hero">
  <svg class="hero-orbit" width="787" height="327" viewBox="0 0 787 327">
    <path d="M0 160 C 200 150, 520 150, 640 165 C 760 185, 720 290, 560 312" fill="none" stroke="#9c9c9c" stroke-width=".8"/>
  </svg>
  <div class="hero-product" role="img" aria-label="Row of five colourful promotional ball pens standing upright"></div>
  <div class="hero-kicker">VELTARO</div>
  <div class="hero-title">PROMOTIONAL</div>
  <div class="hero-sub">BALL PENS</div>
  <p class="hero-copy">We are leading manufacturers and exporters of stationary products.<br>Our existence is global<br><strong>Selling and marketing in all 5 continents</strong></p>
  <div class="btn-outline">CONTACT VELTARO
    <svg width="6" height="10" viewBox="0 0 6 10"><path d="M1 1l4 4-4 4" fill="none" stroke="#dd0a0c" stroke-width="1.4"/></svg>
  </div>
  <div class="hero-dots"><span></span><span></span><span class="on"></span><span></span></div>
  <svg class="hero-arrow" style="left:28px" width="8" height="14" viewBox="0 0 8 14"><path d="M7 1L1 7l6 6" fill="none" stroke="#888" stroke-width="1.2"/></svg>
  <svg class="hero-arrow" style="left:753px" width="8" height="14" viewBox="0 0 8 14"><path d="M1 1l6 6-6 6" fill="none" stroke="#bbb" stroke-width="1.2"/></svg>
</section>

<section class="intro">
  <h2 class="section-title welcome-title">WELCOME TO <em>VELTARO</em></h2>
  <div class="welcome-text">
    <p>Duis autem vel eum iriure dolor in hendrerit in vulputate velit esse molestie consequat, vel illum dolore eu feugiat nulla facilisis at vero eros et accumsan et iusto odio dignissim qui blandit praesent luptatum zzril delenit augue duis dolore te feugait nulla facilisi.</p>
    <p>Lorem ipsum dolor sit amet, consectetuer adipiscing elit, sed diam nonummy nibh euismod tincidunt ut laoreet dolore magna aliquam erat volutpat. Ut wisi enim ad minim veniam, quis nostrud exerci tation ullamcorper suscipit lobortis nisl ut aliquip ex ea commodo consequat. Duis autem vel eum iriure dolor in hendrerit in vulputate velit esse molestie consequat, vel illum dolore eu feugiat nulla facilisis at vero eros et accumsan et iusto odio dignissim qui blandit praesent luptatum zzril delenit augue duis dolore te feugait nulla facilisi.</p>
  </div>
  <div class="divider"></div>

  <h2 class="section-title events-title">EVENTS</h2>
  <span class="round-btn" style="left:686px"><svg width="6" height="9" viewBox="0 0 6 9"><path d="M5 1L1 4.5 5 8" fill="none" stroke="#bbb"/></svg></span>
  <span class="round-btn" style="left:710px"><svg width="6" height="9" viewBox="0 0 6 9"><path d="M1 1l4 3.5L1 8" fill="none" stroke="#bbb"/></svg></span>
  <div class="sort-options">SORT OPTIONS</div>
  <div class="month">JUNE, 2014</div>
  <div class="sort-row"><span class="lbl">SORT BY:</span><span>DATE ▾</span><span class="sep"></span><span>COUNTRY:</span><span class="chip">ALL</span><span>CITY:</span><span class="chip">ALL</span></div>

  <div class="event-list">
    <div class="event" style="top:0">
      <div class="event-date"><span class="dow">FRI</span><span class="day">20</span><span class="mon">JUN</span><span class="range">- 15<br>JUL</span></div>
      <div class="event-name">CAMPING TRIP</div>
      <div class="event-meta">◷ 8:00 am - (July 15) 5:00 am</div>
    </div>
    <div class="event" style="top:46px">
      <div class="event-date"><span class="dow">THU</span><span class="day">26</span><span class="mon">JUN</span></div>
      <div class="event-name">CINCO DE MAYO</div>
      <div class="event-meta">◷ 10:00 am - 3:00 pm &nbsp;⚲ 22 Harbor Lane, Eastfield 40110<br><i>Event Organized By: <b>Riverside Community Guild</b></i></div>
    </div>
  </div>
</section>

<section class="countries">
  <div class="countries-map" role="img" aria-label="Faint world map with connecting network lines"></div>
  <h2 class="countries-title">EXPORTING COUNTRIES</h2>
  <div class="countries-rule"></div>
  <div class="cloud">
    <div class="cloud-row"><span class="lg">Argentina</span><span>Armenia</span><span>Aruba</span><span>Australia</span><span class="lg">Austria</span><span>Azerbaijan</span><span class="lg">Bahamas, The Bahrain</span><span>Bangladesh</span><span class="lg">Barbados</span></div>
    <div class="cloud-row"><span>Belarus</span><span>Belgium</span><span>Belize</span><span>Benin</span><span>Bhutan</span><span>Bolivia</span><span>Bosnia and Herzegovina</span><span class="lg">Botswana</span><span>Brazil</span><span>Brunei</span><span class="lg">Bulgaria</span><span>Burkina</span></div>
    <div class="cloud-row"><span>Cameroon</span><span class="lg">Canada</span><span>Cape Verde</span><span>Central African Republic</span><span class="lg">Chad</span><span class="lg">Chile</span><span>China</span><span>Colombia</span><span>Comoros</span><span>Congo, Democratic Republic</span></div>
    <div class="cloud-row"><span>of the Egypt</span><span>France</span><span>Georgia</span><span class="lg">Germany</span><span>Ghana</span><span>Haiti</span><span>Hong Kong</span><span>Hungary</span><span class="lg">India</span><span>Indonesia</span><span class="lg">Iran</span><span>Iraq</span><span>Ireland</span><span>Italy</span></div>
    <div class="cloud-row"><span class="lg">Jamaica</span><span>Japan</span><span class="lg">Jordan</span></div>
  </div>
</section>

<section class="features">
  <article class="card" style="left:57px">
    <h3 class="card-title">LEADING MANUFACTURERS<br>AND EXPORTERS</h3>
    <div class="seal" role="img" aria-label="Gold seal badge for leading manufacturers"></div>
    <p class="card-text">Cero eros et accumsan et iusto odio dignissimuptatum zzril delenit augue duis dolore te feugait nulla facilisi.</p>
  </article>
  <article class="card" style="left:225px">
    <h3 class="card-title">35 YEARS OF<br>EXPERIENCE</h3>
    <div class="seal" role="img" aria-label="Gold seal badge for 35 years of experience"></div>
    <p class="card-text">Duis autem vel eum iriure dolor in hendrerit in vulputate velit esse molestie consequat, u feugait nulla facilisis .</p>
  </article>
  <article class="card highlight" style="left:395px">
    <h3 class="card-title">HIGH QUALITY<br>STANDARDS</h3>
    <div class="seal" role="img" aria-label="Gold seal badge for quality guarantee"></div>
    <p class="card-text">Cero eros et accumsan et iusto odio dignissim qui blandit praesent luptatum zzril olore te feugait nulla facilisi.</p>
    <div class="plus">+</div>
  </article>
  <article class="card" style="left:563px">
    <h3 class="card-title">CUSTOMER<br>LOYALTY</h3>
    <div class="seal" role="img" aria-label="Gold seal badge for customer loyalty"></div>
    <p class="card-text">Duis autem vel eum iriure dolor in hendrerit in vulputate velit esse molestie consequat, vel illum dolore eu feugiat nulla facilisis .</p>
  </article>
</section>

<footer class="site-footer">
  <div class="footer-brand"><span class="brand-mark"></span><span class="brand-name">VELTARO</span></div>
  <p class="copyright">© 2010 - 2015. VELTARO PENS PVT. LTD. ALL RIGHTS RESERVED.</p>
  <div class="social" aria-label="Social links"><span></span><span></span><span></span><span></span><span></span></div>
</footer>

</body>
</html>
```